Market place for used airplanes/helicopters/parts

http://www.kvistbladet.se needs a facelift.

# What is it
Classifieds for used airplanes/helicopters/parts/spare parts/aviation literature, for people in Scandinavia. The number of classifieds is ~120-200. They are mainly in Swedish, English, Norwegian.

It's not a glamorous or luxurious business, but more for people with a genuine interest in flying, technical things.

Similar to sites like this, but they have much more classifieds than my site
http://www.trevoxlist.com/list/list.aspx?ETID=1&setype=1&catid=6
http://www.bergholmaircraft.com/planes.asp?meny=1&typ=single
https://www.quillhoppers.com/cat.php?mode=listing&main=

# What I want
Design only - no code. I want a modern, maybe a bit bootstrap like, clean, simple, not flashy, web design. I want the design to be in English.

# Audience of the website
Aviation interested men, 45-65 years old, in the nordic countries (around Sweden).

# Logotype that could be used (but not necessarily)
http://www.kvistbladet.se/flygplan_till_salu_large.jpg
http://www.kvistbladet.se/flygplan_till_salu.eps

Reason: I decided to extend the deadline with 1 day. The reason is that I (unfortunately) managed to put the contest in the wrong category for 1 day + I want to give you all feedback (been too busy the whole day, sorry).

Hi all! 

Thanks everyone for the contributions you made. 

I will setup a poll for the designs that I like most. Will get back when I have more information. 

Thanks and have a nice weekend!
Lev

45-65 old Scandinavian men

Business

• - A list with classifieds on the first page, so the visitor easily can see new classifieds.
- A classifieds should be able to have more than one photo
- A simple navigation for showing classifieds from categories like airplanes, helicopters/gyrocopters, parts, literature, misc (maybe other categories) .... but still, it's just 100-200 ads so it's not needed that much filtration.

- A placeholder/way of showing aviation news/clips. In the old design I had, it was a column to the right. It's enough to show maybe 2-5 placeholders.
- A placeholder for PlinkAds ads somewhere on the site.
• - Carousels
- Too much clutter

```html
<!DOCTYPE html>
<html lang="en">
<head>
<meta charset="utf-8">
<title>Kvistbladet – Aircraft Classifieds</title>
<link rel="stylesheet" href="https://fonts.googleapis.com/css2?family=Arimo:wght@400;700&family=Source+Sans+3:wght@400;600&display=swap">
<style>
:root{
  --black:#0b0b0b;
  --panel-dark:#1b1b1b;
  --panel-dark-2:#262626;
  --panel-light:#ebe9e5;
  --panel-light-2:#f2f1ee;
  --line:#c9c6c0;
  --blue:#1e9be0;
  --red:#d8261b;
  --red-dark:#a8170f;
  --text:#1a1a1a;
  --muted:#444;
  --nav-text:#cfcfcf;
}
*{box-sizing:border-box;margin:0;padding:0}
html,body{width:988px;height:1200px;overflow:hidden}
body{position:relative;font-family:"Arimo",Arial,sans-serif;color:var(--text);
  background:linear-gradient(180deg,#a9a9a9 163px,#dcdcdc 240px,#e6e6e6 420px,#c6c6c6 760px,#b9b9b9 1000px,#cfcfcf 1200px)}
.abs{position:absolute}
.topbar{left:0;top:0;width:988px;height:32px;background:var(--black);border-bottom:1px solid #222}
.admin-link{left:767px;top:10px;font-size:10px;color:#8a8a8a;letter-spacing:.3px}
.masthead{left:0;top:32px;width:988px;height:94px;background:linear-gradient(180deg,#1f1f1f,#101010)}
.brand{left:156px;top:60px;display:flex;align-items:center;gap:10px;font-family:"Source Sans 3",sans-serif;font-weight:600;font-size:34px;color:var(--blue);letter-spacing:1px}
.brand-mark{width:18px;height:18px;background:var(--blue)}
.phone{left:609px;top:62px;font-family:"Arimo",sans-serif;font-weight:700;font-size:23px;color:var(--blue)}
.mainnav{left:0;top:126px;width:988px;height:37px;background:linear-gradient(180deg,#2a2a2a,#151515);border-top:1px solid #3a3a3a}
.mainnav ul{position:absolute;left:155px;top:0;display:flex;list-style:none;height:36px;border-left:1px solid #333}
.mainnav li{height:36px;line-height:36px;padding:0 12px;font-family:"Source Sans 3",sans-serif;font-size:12px;color:var(--nav-text);border-right:1px solid #3a3a3a}
.mainnav li.active{background:#3a3a3a;color:#fff;font-weight:600}
.placeholder{display:block}
.banner-ad{left:240px;top:198px;width:516px;height:66px;background:linear-gradient(90deg,#f5b400,#ffc21a);border:1px solid #999}
.tab{position:absolute;left:0;top:0;height:32px;width:121px;background:linear-gradient(180deg,#333,#111);border-radius:6px 6px 0 0;color:#fff;font-family:"Source Sans 3",sans-serif;font-weight:600;font-size:13px;line-height:34px;padding-left:14px;clip-path:polygon(0 0,112px 0,121px 4px,108px 32px,0 32px)}
.featured{left:157px;top:291px;width:678px;height:167px;background:linear-gradient(180deg,#2a2a2a,#111);border-radius:6px;box-shadow:0 8px 10px -6px rgba(0,0,0,.5)}
.feature-card{position:absolute;top:22px;height:127px;border-radius:8px;background:#0d0d0d;border:2px solid #050505;overflow:hidden}
.feature-card .photo{position:absolute;left:2px;top:2px;right:2px;height:80px;border-radius:6px 6px 0 0}
.feature-card .caption{position:absolute;left:14px;top:95px;color:#fff;font-family:"Source Sans 3",sans-serif;font-size:13px}
.go{position:absolute;width:12px;height:13px;background:var(--red)}
.go svg{display:block}
.carousel-arrow{position:absolute;top:67px;width:28px;height:34px;background:#151515;border:1px solid #444}
.listings{left:157px;top:491px;width:424px;height:602px;background:linear-gradient(180deg,var(--panel-light-2),var(--panel-light));border:1px solid #aaa;border-radius:6px}
.listing{position:absolute;left:14px;width:394px;height:124px;border-bottom:1px solid var(--line)}
.listing .thumb{position:absolute;left:0;top:0;width:109px;height:102px}
.price{position:absolute;left:-8px;top:75px;width:85px;height:21px;background:linear-gradient(180deg,var(--red),var(--red-dark));color:#fff;font-size:12.5px;line-height:21px;padding-left:14px}
.listing h3{position:absolute;left:117px;top:1px;font-size:12.5px;font-weight:700;color:#111;letter-spacing:.1px}
.listing p{position:absolute;left:117px;top:24px;width:275px;font-size:9px;line-height:11.6px;color:var(--muted)}
.listing .posted{position:absolute;left:117px;top:91px;font-size:8.5px;color:#222}
.listing .posted span{color:#666}
.more{position:absolute;right:16px;bottom:11px;font-family:"Source Sans 3",sans-serif;font-size:10px;color:#999}
.news{left:586px;top:495px;width:240px;height:340px;background:linear-gradient(180deg,var(--panel-dark-2),var(--panel-dark));border-radius:6px;border:1px solid #000}
.news-item{position:absolute;left:14px;width:212px;height:95px;border-bottom:1px solid #555}
.news-item .thumb{position:absolute;left:0;top:0;width:58px;height:64px}
.news-item p{position:absolute;left:72px;top:-1px;width:142px;font-size:8.5px;line-height:11.6px;color:#ddd}
.news-item .author{position:absolute;right:0;top:55px;font-size:9.5px;font-weight:700;color:var(--red)}
.ads{left:586px;top:848px;width:240px;height:202px;background:linear-gradient(180deg,var(--panel-light-2),var(--panel-light));border:1px solid #aaa;border-radius:6px}
.side-ad{position:absolute;left:36px;top:37px;width:169px;height:142px;background:linear-gradient(180deg,#fff 0,#fff 20%,#2a6fbf 21%,#1d4f96 100%)}
.plane-art{left:370px;top:1097px;width:215px;height:70px;background:radial-gradient(ellipse at center,#8d8d8d 0,#b0b0b0 45%,rgba(190,190,190,0) 70%)}
.footer{left:155px;top:1165px;width:678px;height:35px;background:linear-gradient(180deg,#2a2a2a,#111);border-radius:6px 6px 0 0}
.footer .copy{position:absolute;left:14px;top:15px;font-size:9px;color:#ccc}
.footer .copy b{color:#fff}
.footer .links{position:absolute;right:10px;top:15px;font-size:9px;color:#eee;word-spacing:1px}
</style>
</head>
<body>
<div class="abs topbar"></div>
<div class="abs admin-link">Admin login</div>
<header class="abs masthead"></header>
<div class="abs brand"><span class="brand-mark"></span>KVISTBLADET</div>
<div class="abs phone">Call 0700-318452</div>
<nav class="abs mainnav">
  <ul>
    <li class="active">HOME</li><li>CATEGORIES</li><li>ADD Classified</li><li>Edit Classified</li><li>CONTACT</li>
  </ul>
</nav>

<div class="abs banner-ad placeholder" role="img" aria-label="Banner advertisement, yellow deals ad"></div>

<section class="abs featured">
  <div class="tab">Featured</div>
  <div class="carousel-arrow" style="left:-14px"><svg width="26" height="32"><path d="M15 11l-5 5 5 5" stroke="#fff" stroke-width="2.5" fill="none"/></svg></div>
  <div class="carousel-arrow" style="left:664px"><svg width="26" height="32"><path d="M11 11l5 5-5 5" stroke="#fff" stroke-width="2.5" fill="none"/></svg></div>
  <div class="feature-card" style="left:31px;width:195px">
    <div class="photo" role="img" aria-label="Photo of a small propeller plane on a runway" style="background:linear-gradient(180deg,#9aa3ad,#c9ccd0 55%,#6d6f70)"></div>
    <div class="caption">Listing 1</div>
    <div class="go" style="left:166px;top:96px"><svg width="12" height="13"><path d="M4 3l4 3.5-4 3.5" stroke="#fff" stroke-width="1.6" fill="none"/></svg></div>
  </div>
  <div class="feature-card" style="left:240px;width:198px">
    <div class="photo" role="img" aria-label="Photo of red seats inside an aircraft cabin" style="background:linear-gradient(90deg,#8a1418,#c2282b 45%,#d9d3cb)"></div>
    <div class="caption">Listing 2</div>
    <div class="go" style="left:166px;top:96px"><svg width="12" height="13"><path d="M4 3l4 3.5-4 3.5" stroke="#fff" stroke-width="1.6" fill="none"/></svg></div>
  </div>
  <div class="feature-card" style="left:452px;width:198px">
    <div class="photo" role="img" aria-label="Photo of light aircraft parked in a mountain valley" style="background:linear-gradient(180deg,#9fb7cc,#8a6f55 45%,#7e6a55)"></div>
    <div class="caption">Listing 3</div>
    <div class="go" style="left:166px;top:96px"><svg width="12" height="13"><path d="M4 3l4 3.5-4 3.5" stroke="#fff" stroke-width="1.6" fill="none"/></svg></div>
  </div>
</section>

<section class="abs listings">
  <div class="tab" style="top:-4px">LISTINGS</div>
  <article class="listing" style="top:46px">
    <div class="thumb" role="img" aria-label="Photo of a white light aircraft in a hangar" style="background:linear-gradient(180deg,#3a3a3a,#8c8c8c 60%,#4a4a4a)"></div>
    <div class="price">€ 30,000</div>
    <h3>Nam pulvinar justo a ipsum aliquet vtitae</h3>
    <p>Curabitur a diam turpis. Mauris tempor ligula vehicula velit mollis semper. Duis congue, tortor bibendum sagittis blandit, mauris felis imperdiet diam, et lacinia urna nibh vel sapien. Suspendisse porttitor adipiscing orci.</p>
    <div class="posted">Posted in <span>Helicopterst</span></div>
    <div class="go" style="left:383px;top:88px"><svg width="12" height="13"><path d="M4 3l4 3.5-4 3.5" stroke="#fff" stroke-width="1.6" fill="none"/></svg></div>
  </article>
  <article class="listing" style="top:180px">
    <div class="thumb" role="img" aria-label="Photo of an aircraft engine" style="background:radial-gradient(circle at 50% 45%,#8a2a22,#c9c9c9 55%,#f4f4f4)"></div>
    <div class="price">€ 1257</div>
    <h3>Nam pulvinar justo a ipsum aliquet vtitae</h3>
    <p>Curabitur a diam turpis. Mauris tempor ligula vehicula velit mollis semper. Duis congue, tortor bibendum sagittis blandit, mauris felis imperdiet diam, et lacinia urna nibh vel sapien. Suspendisse porttitor adipiscing orci.</p>
    <div class="posted">Posted in <span>Airplanes</span></div>
    <div class="go" style="left:383px;top:88px"><svg width="12" height="13"><path d="M4 3l4 3.5-4 3.5" stroke="#fff" stroke-width="1.6" fill="none"/></svg></div>
  </article>
  <article class="listing" style="top:312px">
    <div class="thumb" role="img" aria-label="Photo of a small aircraft outside a hangar" style="background:linear-gradient(180deg,#6b4632,#b89372 50%,#8b6a4e)"></div>
    <div class="price">€ 12,590</div>
    <h3>Nam pulvinar justo a ipsum aliquet vtitae</h3>
    <p>Curabitur a diam turpis. Mauris tempor ligula vehicula velit mollis semper. Duis congue, tortor bibendum sagittis blandit, mauris felis imperdiet diam, et lacinia urna nibh vel sapien. Suspendisse porttitor adipiscing orci.</p>
    <div class="posted">Posted in <span>spare parts</span></div>
    <div class="go" style="left:383px;top:88px"><svg width="12" height="13"><path d="M4 3l4 3.5-4 3.5" stroke="#fff" stroke-width="1.6" fill="none"/></svg></div>
  </article>
  <article class="listing" style="top:446px;left:11px">
    <div class="thumb" role="img" aria-label="Photo of a used piston engine" style="background:linear-gradient(180deg,#5c5144,#8a7c68 50%,#3e352c)"></div>
    <div class="price">€ 400</div>
    <h3>Nam pulvinar justo a ipsum aliquet vtitae</h3>
    <p>Curabitur a diam turpis. Mauris tempor ligula vehicula velit mollis semper. Duis congue, tortor bibendum sagittis blandit, mauris felis imperdiet diam, et lacinia urna nibh vel sapien. Suspendisse porttitor adipiscing orci.</p>
    <div class="posted">Posted in <span>spare parts</span></div>
    <div class="go" style="left:383px;top:88px"><svg width="12" height="13"><path d="M4 3l4 3.5-4 3.5" stroke="#fff" stroke-width="1.6" fill="none"/></svg></div>
  </article>
  <div class="more">MORE &nbsp;›</div>
</section>

<aside class="abs news">
  <div class="tab" style="top:-4px">NEWS</div>
  <div class="news-item" style="top:46px">
    <div class="thumb" role="img" aria-label="Photo of a helicopter on display" style="background:linear-gradient(180deg,#a9c2d8,#5f6f55 70%,#4d4d3c)"></div>
    <p>Nam pulvinar justo a ipsum aliquet vitae lacinia mauris dignissim. Maecenas nec purus at nisi .</p>
    <div class="go" style="left:72px;top:50px"><svg width="12" height="13"><path d="M4 3l4 3.5-4 3.5" stroke="#fff" stroke-width="1.6" fill="none"/></svg></div>
    <div class="author">Lev Dahlqvist</div>
  </div>
  <div class="news-item" style="top:142px">
    <div class="thumb" role="img" aria-label="Photo of a light aircraft parked on grass" style="background:linear-gradient(180deg,#c8ccd0,#dcdcdc 50%,#7d7f74)"></div>
    <p>Nam pulvinar justo a ipsum aliquet vitae lacinia mauris dignissim. Maecenas nec purus at nisi .</p>
    <div class="go" style="left:72px;top:50px"><svg width="12" height="13"><path d="M4 3l4 3.5-4 3.5" stroke="#fff" stroke-width="1.6" fill="none"/></svg></div>
    <div class="author">Lev Dahlqvist</div>
  </div>
  <div class="news-item" style="top:238px;border-bottom:none">
    <div class="thumb" role="img" aria-label="Photo of a jet climbing into blue sky" style="background:radial-gradient(circle,#cfe6ff,#3d8ee0 55%,#1d5fb4)"></div>
    <p>Nam pulvinar justo a ipsum aliquet vitae lacinia mauris dignissim. Maecenas nec purus at nisi .</p>
    <div class="go" style="left:72px;top:50px"><svg width="12" height="13"><path d="M4 3l4 3.5-4 3.5" stroke="#fff" stroke-width="1.6" fill="none"/></svg></div>
    <div class="author">Lev Dahlqvist</div>
  </div>
</aside>

<aside class="abs ads">
  <div class="tab" style="top:-1px">ADS</div>
  <div class="side-ad" role="img" aria-label="Sidebar advertisement for a car"></div>
</aside>

<div class="abs plane-art placeholder" role="img" aria-label="Illustration of a small single-engine plane"></div>

<footer class="abs footer">
  <div class="copy">Copyright 2013 <b>www.kvistbladet.se</b></div>
  <div class="links">Home &nbsp;| &nbsp;Categories &nbsp;| &nbsp;Add Classified &nbsp;| &nbsp;Edit Classified &nbsp;| &nbsp;Contact</div>
</footer>
</body>
</html>
```